Ad for regional magazine for startup "Varumo"

We need a small ad for a small German regional magazine for our startup company Varumo which provides on-premise service for all kind of electronic problems.

We also need the Indesign files to be able to make minor changes (e.g. the phone number) in the future.

An example ad that we used before (for another region with another phone number) is attached.

Industry/Entity Type

Technical Service

Requirements
Must have
• Needed contents:
• "Elektronik-Problem?" (Electronic problem?)
• "Ihr Media-Pannenhelfer kommt" (Your media helper comes)
• "TV, Video, Telefon, Smartphone, Internet, Computer"
• "Terminbuchung: 07041-3926518" (booking)
• "Soforthilfe - auch abends und am Wochenende" (immediate help - also in the evenings and at the weekend)
• "www.varumo.de"
• logo
• picture
• Size: 90mm (width) x 50-70mm (height)
• Font & colors: see attachment

```html
<!DOCTYPE html>
<html lang="de">
<head>
<meta charset="utf-8">
<title>Varumo – Anzeige</title>
<link rel="stylesheet" href="https://fonts.googleapis.com/css2?family=Noto+Sans:wght@400;600;700&display=swap">
<style>
  :root {
    --page-bg: #e6e6e6;
    --card-bg: #ffffff;
    --card-border: #8a8a8a;
    --ink-dark: #3f454b;
    --ink-green: #2f9a44;
    --photo-light: #f1eeea;
    --photo-mid: #dcd5cb;
    --photo-deep: #c9bfb1;
  }
  * { box-sizing: border-box; margin: 0; padding: 0; }
  html, body {
    width: 1200px;
    height: 960px;
    overflow: hidden;
    background: var(--page-bg);
    font-family: "Noto Sans", "Verdana", sans-serif;
  }
  .ad {
    position: absolute;
    left: 60px;
    top: 163px;
    width: 1080px;
    height: 634px;
    background: var(--card-bg);
    border: 2px solid var(--card-border);
    color: var(--ink-dark);
  }
  .ad-headline {
    position: absolute;
    left: 0; right: 0; top: 18px;
    text-align: center;
    font-size: 56px;
    font-weight: 600;
    line-height: 1.1;
    letter-spacing: 0.5px;
  }
  .ad-subline {
    position: absolute;
    left: 0; right: 0; top: 82px;
    text-align: center;
    font-size: 46px;
    font-weight: 700;
    color: var(--ink-green);
    line-height: 1.1;
  }
  .ad-services {
    position: absolute;
    left: 0; right: 0; top: 142px;
    text-align: center;
    font-size: 27px;
    font-weight: 700;
    line-height: 1.1;
  }
  .ad-photo {
    position: absolute;
    left: 128px;
    top: 187px;
    width: 820px;
    height: 319px;
    background: linear-gradient(100deg, var(--photo-light) 0%, var(--photo-mid) 45%, var(--photo-light) 70%, var(--photo-deep) 100%);
  }
  .ad-booking {
    position: absolute;
    left: 128px;
    top: 518px;
    font-size: 30px;
    font-weight: 700;
    line-height: 1.1;
  }
  .ad-hours {
    position: absolute;
    left: 128px;
    top: 558px;
    font-size: 24px;
    font-weight: 700;
    line-height: 1.2;
  }
  .ad-web {
    position: absolute;
    left: 684px;
    top: 516px;
    font-size: 32px;
    font-weight: 700;
    line-height: 1.1;
  }
  .ad-brand {
    position: absolute;
    left: 684px;
    top: 552px;
    font-size: 62px;
    font-weight: 700;
    line-height: 1.1;
    letter-spacing: 2px;
    color: var(--ink-dark);
  }
</style>
</head>
<body>
  <article class="ad">
    <h1 class="ad-headline">Elektronik-Problem?</h1>
    <h2 class="ad-subline">Ihr Media-Pannenhelfer kommt</h2>
    <p class="ad-services">TV, Video, Telefon, Smartphone, Internet, Computer</p>
    <div class="ad-photo" role="img" aria-label="Foto: Ein Servicetechniker erklärt einem älteren Herrn am Esstisch ein Smartphone"></div>
    <p class="ad-booking">Terminbuchung: 07041-3926518</p>
    <p class="ad-hours">Soforthilfe - auch abends<br>und am Wochenende</p>
    <p class="ad-web">www.varumo.de</p>
    <p class="ad-brand">varumo</p>
  </article>
</body>
</html>
```